Software engineering company needs business card

I need a cool business card. Company: Byte Merano Larchwood Ave 41 58213 Dunmere Name: Gerald Hofmann CEO / Managing Director & Owner

Industry/Entity Type

Business

```html
<!DOCTYPE html>
<html lang="en">
<head>
<meta charset="utf-8">
<title>Byte Merano – Business Card</title>
<link rel="stylesheet" href="https://fonts.googleapis.com/css2?family=Open+Sans:wght@400;600;700&display=swap">
<style>
  :root {
    --lime: #8dc63f;
    --slate: #58595b;
    --ink: #4d4d4f;
    --paper: #ffffff;
    --backdrop: #e6e6e4;
  }
  * { margin: 0; padding: 0; box-sizing: border-box; }
  html, body {
    width: 1200px;
    height: 902px;
    overflow: hidden;
    background: var(--backdrop);
    font-family: "Open Sans", Arial, sans-serif;
  }
  .business-card {
    position: absolute;
    left: 70px;
    top: 150px;
    width: 1060px;
    height: 603px;
    background: var(--paper);
    box-shadow: 0 10px 30px rgba(0,0,0,0.18);
    overflow: hidden;
  }
  .card-shapes {
    position: absolute;
    inset: 0;
    width: 100%;
    height: 100%;
  }
  .shape-lime { fill: var(--lime); }
  .shape-slate { fill: var(--slate); }

  .brand {
    position: absolute;
    left: 470px;
    top: 118px;
    display: flex;
    align-items: center;
    gap: 22px;
  }
  .brand-square {
    width: 52px;
    height: 52px;
    background: var(--lime);
  }
  .brand-name {
    font-size: 66px;
    font-weight: 600;
    color: var(--slate);
    letter-spacing: 1px;
    line-height: 1;
  }

  .person {
    position: absolute;
    left: 56px;
    top: 312px;
  }
  .person-name {
    font-size: 35px;
    font-weight: 700;
    line-height: 1.1;
    color: var(--ink);
  }
  .person-name .first { color: var(--lime); }
  .person-role {
    margin-top: 4px;
    font-size: 27px;
    font-weight: 400;
    color: var(--ink);
  }

  .contact-list {
    position: absolute;
    left: 56px;
    top: 424px;
    list-style: none;
  }
  .contact-item {
    display: flex;
    align-items: center;
    gap: 10px;
    height: 35px;
    font-size: 27px;
    color: var(--ink);
  }
  .contact-icon {
    width: 29px;
    height: 29px;
    flex: none;
    background: var(--lime);
  }
  .contact-icon svg { width: 29px; height: 29px; display: block; }
  .contact-icon .stroke { fill: none; stroke: #fff; stroke-width: 1.6; stroke-linejoin: round; }
</style>
</head>
<body>
  <article class="business-card">
    <svg class="card-shapes" viewBox="0 0 940 535" preserveAspectRatio="none" aria-hidden="true">
      <path class="shape-lime" d="M0 0 H940 V15 C720 8 420 8 220 80 C120 118 45 165 0 208 Z"/>
      <path class="shape-slate" d="M0 507 C160 512 360 515 520 478 C710 435 860 330 940 215 V535 H0 Z"/>
    </svg>

    <div class="brand">
      <span class="brand-square" aria-hidden="true"></span>
      <span class="brand-name">Byte Merano</span>
    </div>

    <div class="person">
      <p class="person-name"><span class="first">Gerald</span> Hofmann</p>
      <p class="person-role">CEO / Managing Director &amp; Owner</p>
    </div>

    <ul class="contact-list">
      <li class="contact-item">
        <span class="contact-icon" aria-hidden="true">
          <svg viewBox="0 0 29 29"><path class="stroke" d="M8 9 C8 7 10 6 14.5 6 C19 6 21 7 21 9 L19 10.5 L17 9.5 L17 8 H12 V9.5 L10 10.5 Z"/><rect class="stroke" x="8" y="13" width="13" height="9" rx="1"/><circle class="stroke" cx="14.5" cy="17.5" r="2"/></svg>
        </span>
        (02) 4861 3570
      </li>
      <li class="contact-item">
        <span class="contact-icon" aria-hidden="true">
          <svg viewBox="0 0 29 29"><rect class="stroke" x="6" y="9" width="17" height="12"/><path class="stroke" d="M6 9 L14.5 16 L23 9"/></svg>
        </span>
        Info@bytemerano.com
      </li>
      <li class="contact-item">
        <span class="contact-icon" aria-hidden="true">
          <svg viewBox="0 0 29 29"><circle class="stroke" cx="14.5" cy="14.5" r="8"/><ellipse class="stroke" cx="14.5" cy="14.5" rx="3.5" ry="8"/><path class="stroke" d="M6.5 14.5 H22.5 M8 10 H21 M8 19 H21"/></svg>
        </span>
        www.bytemerano.com
      </li>
    </ul>
  </article>
</body>
</html>
```